Clamshell Packaging Design Project

We are looking for a design for the laminated card inserts we use in our clamshell packaging.

We want to include our logo, obviously, and a background image to make the packaging really stand out. Something that conveys the superiority and premium quality of the product inside

We'd also like to include a blank space so we can affix item description stickers to the front of the packaging if necessary.

Card size will be 120mm tall x 100mm wide.

We sell replacement guitar parts worldwide, mainly to males aged 16-60 and would like a design with a professional feel.

our web address is www.brambleforkstrings.co.uk should you wish to take a look.

Target Market(s)

males ages 16-60 worldwide

Industry/Entity Type

Product

Requirements
Must have
• logo
web address
sapce for item description
Phone number

```html
<!DOCTYPE html>
<html lang="en">
<head>
<meta charset="utf-8">
<title>Bramblefork Strings – Clamshell Card Insert</title>
<link href="https://fonts.googleapis.com/css2?family=Bodoni+Moda:opsz,wght@6..96,500;6..96,700&display=swap" rel="stylesheet">
<style>
  :root {
    --backdrop: #2a1a14;
    --card: #000000;
    --headline: #ffffff;
    --brand-red: #d3202b;
    --tagline: #ffffff;
    --contact: #ffffff;
    --sticker-space: #ffffff;
    --figure-top: #e9e6f4;
    --figure-mid: #c23ad6;
    --figure-low: #7a3a18;
  }
  * { margin: 0; padding: 0; box-sizing: border-box; }
  html, body {
    width: 1200px;
    height: 742px;
    overflow: hidden;
    background: var(--backdrop);
  }
  .canvas {
    position: relative;
    width: 1200px;
    height: 742px;
  }
  .insert-card {
    position: absolute;
    left: 46px;
    top: 95px;
    width: 462px;
    height: 551px;
    background: var(--card);
    border-radius: 22px;
    overflow: hidden;
  }
  .hero-figure {
    position: absolute;
    left: 232px;
    top: 27px;
    width: 180px;
    height: 524px;
    border-radius: 60px 60px 20px 20px;
    background: linear-gradient(180deg,
      var(--figure-top) 0%,
      #d9c6ef 30%,
      var(--figure-mid) 52%,
      #9b3a6a 72%,
      var(--figure-low) 100%);
    opacity: 0.9;
  }
  .headline {
    position: absolute;
    left: 30px;
    top: 126px;
    font-family: "Bodoni Moda", "Didot", serif;
    font-weight: 700;
    font-size: 65px;
    line-height: 65px;
    letter-spacing: -1.5px;
    white-space: nowrap;
    color: var(--headline);
  }
  .brand {
    position: absolute;
    left: 44px;
    top: 362px;
    white-space: nowrap;
  }
  .brand-name {
    font-family: "Bodoni Moda", "Didot", serif;
    font-weight: 700;
    font-size: 24px;
    line-height: 26px;
    color: var(--brand-red);
  }
  .brand-tagline {
    margin-top: 4px;
    font-family: "Bodoni Moda", "Didot", serif;
    font-weight: 700;
    font-size: 10px;
    color: var(--tagline);
  }
  .sticker-space {
    position: absolute;
    left: 37px;
    top: 442px;
    width: 377px;
    height: 56px;
    border-radius: 28px;
    background: var(--sticker-space);
  }
  .contact {
    position: absolute;
    left: 37px;
    top: 512px;
    width: 377px;
    text-align: center;
    font-family: "Bodoni Moda", "Didot", serif;
    font-weight: 700;
    font-size: 13px;
    line-height: 16px;
    white-space: nowrap;
    color: var(--contact);
  }
</style>
</head>
<body>
  <div class="canvas">
    <section class="insert-card">
      <div class="hero-figure" role="img" aria-label="Silhouette of a rock guitarist raising a guitar overhead, filled with pink and violet stage light"></div>
      <h1 class="headline">Yes,<br>We have<br>Quality Parts</h1>
      <div class="brand">
        <div class="brand-name">Bramblefork Strings</div>
        <div class="brand-tagline">Retro-fit parts from the UK</div>
      </div>
      <div class="sticker-space" aria-label="Space for item description sticker"></div>
      <p class="contact">www.brambleforkstrings.co.uk &nbsp;·&nbsp; 0161 496 0142</p>
    </section>
  </div>
</body>
</html>
```